Bierlogo gesucht
Zielgruppe
Bierherstellung / Zielgruppe sowohl Konsumenten von traditionellen Sorten als auch Liebhaber von Craftbeer
Aufgabenstellung
Aufgabe ist die Gestaltung eines Bieretiketts für den Brustbereich der Flasche / Weitere Auftragserweiterung Website und Cooperate Identity gewünscht / Lebensmittelrechtlich relevante Angaben sind zu berücksichtigen / Herstellung im Raum Oberbayern - Ammersee
Logo in Verbindung mit dem Namen "Haldbrunner" soll sowohl Qualität als auch Offenheit für neue Einflüsse, Rezepte, Inhaltsstoffe vermitteln, Stil kann gerne sehr einfach bzgl. Farbgebung aber einprägsam sein

```html
<!DOCTYPE html>
<html lang="de">
<head>
<meta charset="utf-8">
<title>Haldbrunner Bier – Summer Ale Etikett</title>
<link rel="stylesheet" href="https://fonts.googleapis.com/css2?family=Archivo:wght@800&family=Kaushan+Script&family=Cinzel:wght@400&family=Fira+Sans+Condensed:wght@400;600;700&display=swap">
<style>
  :root {
    --label-black: #000000;
    --label-white: #ffffff;
    --band-green: #155d04;
    --page-bg: #ffffff;
    --art-tone: #2a2a2a;
  }
  html, body {
    margin: 0;
    padding: 0;
    width: 1200px;
    height: 908px;
    overflow: hidden;
    background: var(--page-bg);
  }
  .label {
    display: block;
    width: 1200px;
    height: 908px;
  }
  .label__shape { fill: var(--label-black); }
  .label__band { fill: var(--band-green); }
  .label__art { fill: var(--art-tone); }
  .label__kicker {
    font-family: "Archivo", Arial, sans-serif;
    font-weight: 800;
    font-size: 47px;
    fill: var(--label-white);
    letter-spacing: 1px;
  }
  .label__name {
    font-family: "Kaushan Script", cursive;
    fill: var(--label-white);
  }
  .label__name--brand { font-size: 128px; }
  .label__name--sub { font-size: 150px; }
  .label__style {
    font-family: "Cinzel", Georgia, serif;
    font-size: 62px;
    fill: var(--label-white);
  }
  .label__facts {
    font-family: "Fira Sans Condensed", Arial, sans-serif;
    fill: var(--label-white);
    font-size: 19px;
  }
  .label__facts-title { font-weight: 700; font-size: 18px; }
  .label__volume {
    font-family: "Fira Sans Condensed", Arial, sans-serif;
    font-weight: 700;
    font-size: 34px;
    fill: var(--label-white);
  }
</style>
</head>
<body>
<svg class="label" viewBox="0 0 1200 908" xmlns="http://www.w3.org/2000/svg">
  <defs>
    <clipPath id="diamond-clip">
      <polygon points="600,18 1200,459 600,898 0,459"/>
    </clipPath>
    <path id="style-arc" d="M 183,1092 A 417,417 0 0 1 1017,1092"/>
  </defs>

  <polygon class="label__shape" points="600,18 1200,459 600,898 0,459"/>

  <g clip-path="url(#diamond-clip)">
    <path class="label__band" fill-rule="evenodd"
      d="M 132,1065 A 468,468 0 1 1 1068,1065 A 468,468 0 1 1 132,1065 Z
         M 213,1092 A 387,387 0 1 0 987,1092 A 387,387 0 1 0 213,1092 Z"/>
  </g>

  <rect class="label__art" x="390" y="81" width="417" height="156" rx="6"
    role="img" aria-label="Illustration: zwei Hopfendolden über gekreuzten Gerstenähren"/>

  <text class="label__kicker" x="596" y="294" text-anchor="middle">CRAFTBEER</text>

  <text class="label__name label__name--brand" x="600" y="420" text-anchor="middle" textLength="880" lengthAdjust="spacingAndGlyphs">Haldbrunner</text>
  <text class="label__name label__name--sub" x="594" y="585" text-anchor="middle">Bier</text>

  <text class="label__style">
    <textPath href="#style-arc" startOffset="50%" text-anchor="middle">SUMMER ALE</textPath>
  </text>

  <g class="label__facts" text-anchor="middle">
    <text class="label__facts-title" x="600" y="737">ZUTATEN:</text>
    <text x="600" y="759">Wasser, Gerstenmalz, Hopfen, Hefe</text>
    <text x="600" y="782">D-86999 Haldbrunn</text>
    <text x="600" y="805">Alk. 4,9% vol.</text>
  </g>
  <text class="label__volume" x="600" y="850" text-anchor="middle">℮  50 cl</text>
</svg>
</body>
</html>
```